Sale Hang Tag

Design a bright, cheerful, compelling, call to action sale tag for a lighting showroom. The tag will be used to move older or discontinued product at a really good price. Upscale, friendly, neighbor store. Size should be no larger than 4 by 6 inches.

Industry/Entity Type

Call

```html
<!DOCTYPE html>
<html lang="en">
<head>
<meta charset="utf-8">
<title>Sale Hang Tag</title>
<link rel="stylesheet" href="https://fonts.googleapis.com/css2?family=Libre+Baskerville:wght@700&display=swap">
<style>
  :root {
    --bg-light: #6dba44;
    --bg-dark: #0f9446;
    --tag-paper: #ffffff;
    --string: #ffffff;
    --red: #e8202a;
    --orange: #f7941d;
    --yellow: #ffd400;
    --green: #3aaa4a;
    --lime: #c9d82b;
  }
  html, body {
    margin: 0;
    padding: 0;
    width: 1200px;
    height: 900px;
    overflow: hidden;
  }
  .canvas {
    position: relative;
    width: 1200px;
    height: 900px;
    background: linear-gradient(90deg, var(--bg-light), var(--bg-dark));
  }
  .hang-tag {
    position: absolute;
    top: 340px;
    width: 290px;
    height: 435px;
    background: var(--tag-paper);
    box-shadow: 4px 6px 6px rgba(0, 0, 0, 0.35);
  }
  .hang-tag--warm { left: 225px; --ink: var(--red); --accent: var(--orange); --glow: var(--yellow); }
  .hang-tag--fresh { left: 696px; --ink: var(--green); --accent: var(--lime); --glow: var(--yellow); }
  .tag-string {
    position: absolute;
    left: 110px;
    top: -210px;
    width: 44px;
    height: 212px;
    overflow: visible;
  }
  .dot-rails {
    position: absolute;
    inset: 0;
    width: 290px;
    height: 435px;
  }
  .chandelier-art {
    position: absolute;
    left: 84px;
    top: 0;
    width: 206px;
    height: 318px;
    background:
      radial-gradient(ellipse 48% 40% at 50% 62%, var(--ink) 0%, var(--ink) 45%, var(--glow) 75%, rgba(255,255,255,0) 100%);
  }
  .sale-word {
    position: absolute;
    left: 104px;
    top: 352px;
    margin: 0;
    font-family: "Libre Baskerville", "Times New Roman", serif;
    font-weight: 700;
    font-size: 50px;
    line-height: 1;
    letter-spacing: 1px;
    color: var(--ink);
  }
</style>
</head>
<body>
<main class="canvas">

  <section class="hang-tag hang-tag--warm">
    <svg class="tag-string" viewBox="0 0 44 212" aria-hidden="true">
      <path d="M7 212 L5 40 Q5 4 22 4 Q39 4 39 40 L37 212" fill="none" stroke="var(--string)" stroke-width="3"/>
    </svg>
    <div class="chandelier-art" role="img" aria-label="Red and yellow chandelier illustration hanging from the top edge"></div>
    <svg class="dot-rails" viewBox="0 0 290 435" aria-hidden="true">
      <line x1="76" y1="8" x2="76" y2="428" stroke="var(--ink)" stroke-width="10" stroke-linecap="round" stroke-dasharray="0 12.5"/>
      <line x1="76" y1="33" x2="76" y2="428" stroke="var(--glow)" stroke-width="10.5" stroke-linecap="round" stroke-dasharray="0 50"/>
      <line x1="76" y1="58" x2="76" y2="428" stroke="var(--accent)" stroke-width="10.5" stroke-linecap="round" stroke-dasharray="0 75"/>
      <line x1="5" y1="328" x2="286" y2="328" stroke="var(--ink)" stroke-width="7" stroke-linecap="round" stroke-dasharray="0 9"/>
      <line x1="14" y1="328" x2="286" y2="328" stroke="var(--glow)" stroke-width="7.5" stroke-linecap="round" stroke-dasharray="0 36"/>
      <circle cx="76" cy="328" r="6" fill="var(--glow)"/>
    </svg>
    <p class="sale-word">SALE</p>
  </section>

  <section class="hang-tag hang-tag--fresh">
    <svg class="tag-string" viewBox="0 0 44 212" aria-hidden="true">
      <path d="M7 212 L5 40 Q5 4 22 4 Q39 4 39 40 L37 212" fill="none" stroke="var(--string)" stroke-width="3"/>
    </svg>
    <div class="chandelier-art" role="img" aria-label="Green and yellow chandelier illustration hanging from the top edge"></div>
    <svg class="dot-rails" viewBox="0 0 290 435" aria-hidden="true">
      <line x1="76" y1="8" x2="76" y2="428" stroke="var(--ink)" stroke-width="10" stroke-linecap="round" stroke-dasharray="0 12.5"/>
      <line x1="76" y1="33" x2="76" y2="428" stroke="var(--accent)" stroke-width="10.5" stroke-linecap="round" stroke-dasharray="0 50"/>
      <line x1="76" y1="58" x2="76" y2="428" stroke="var(--glow)" stroke-width="10.5" stroke-linecap="round" stroke-dasharray="0 75"/>
      <line x1="5" y1="328" x2="286" y2="328" stroke="var(--ink)" stroke-width="7" stroke-linecap="round" stroke-dasharray="0 9"/>
      <line x1="14" y1="328" x2="286" y2="328" stroke="var(--glow)" stroke-width="7.5" stroke-linecap="round" stroke-dasharray="0 36"/>
      <circle cx="76" cy="328" r="6" fill="var(--glow)"/>
    </svg>
    <p class="sale-word">SALE</p>
  </section>

</main>
</body>
</html>
```